PLUME study results infographic

We enjoyed the previous infographic design you provided for us (The GLaRN cohort study Infographic), and would like to invite you to design another infographic in a similar style and layout.
We need an infographic which presents the results from the PLUME research trial. It should be colourful and engaging, in understandable language and showing the steps to get to the results. This is to showcase the results to patients/the public/clinicians, giving a brief summary of what the study proved. The final design should have the PLUME logo at the top (please see attached and https://plume.vextru.qb.zz.example/welcome-plume-trial)
I have attached the required logos which need to be used (PLUME, Carrowby Injury and Acute Care, University of Carrowby) as well as an example from another study, The GLaRN cohort study Infographic, as an example of what the layout could look like. Please DO NOT use the content from the The GLaRN cohort study Infographic example though, please instead use the content from the attached document 'PLUME_InfographicDesignInformation_PitchHive'.

```html
<!DOCTYPE html>
<html lang="en">
<head>
<meta charset="utf-8">
<title>PLUME Randomized Controlled Trial Infographic</title>
<link rel="stylesheet" href="https://fonts.googleapis.com/css2?family=Poppins:wght@400;500;600;700;800&display=swap">
<style>
:root{
  --navy:#1f3864;
  --sky:#2eaae2;
  --teal:#138a85;
  --ring:#2a9fe0;
  --ink:#1f2f4f;
  --text:#222;
  --white:#fff;
  --line:#9fc7ea;
}
*{box-sizing:border-box;margin:0;padding:0}
html,body{width:1200px;height:2834px;overflow:hidden}
body{font-family:'Poppins',sans-serif;color:var(--text);background:var(--white);position:relative}
.abs{position:absolute}

/* header */
.masthead{left:0;top:0;width:1200px;height:376px;background:var(--navy)}
.brand{left:0;width:1200px;top:88px;display:flex;justify-content:center;align-items:center;gap:14px}
.brand-dot{width:34px;height:34px;border-radius:50%;background:var(--sky)}
.brand-name{font-weight:700;font-size:54px;line-height:64px;color:var(--white);letter-spacing:2px}
.masthead-title{left:40px;width:1120px;top:200px;text-align:center;color:var(--white);font-weight:800;font-size:29.5px;line-height:29px;text-transform:uppercase;white-space:nowrap}
.masthead-title span{display:block;color:var(--sky)}

/* intro */
.intro-heading{left:79px;top:434px;font-weight:800;font-size:30px;line-height:39px;color:var(--ink)}
.intro-heading span{display:block;color:var(--sky)}
.intro-body{left:72px;top:610px;width:560px;border-left:4px solid var(--sky);padding-left:16px;font-size:19px;line-height:29px;color:#333}
.intro-art{left:650px;top:423px;width:505px;height:413px;border-radius:12px;background:linear-gradient(135deg,#cfe6fb,#8fc3f2 60%,#e9f2f8)}

/* findings */
.findings{left:0;top:900px;width:1200px;height:409px;background:linear-gradient(#e7f2fc,#d7e9f8)}
.tab{height:50px;border-radius:0 0 40px 40px;color:var(--white);font-weight:700;font-size:20px;display:flex;align-items:center;justify-content:center;letter-spacing:.5px}
.tab-teal{background:var(--teal)}
.tab-navy{background:var(--navy)}
.findings .tab{position:absolute;left:465px;top:0;width:278px}
.track{left:182px;top:1111px;width:850px;border-top:2px dashed var(--line)}
.node{width:116px;height:116px;border-radius:50%;background:var(--white);border:6px solid var(--ring);display:flex;align-items:center;justify-content:center}
.stem{width:2px;height:22px;background:var(--ring)}
.stem::after{content:"";position:absolute;left:-3px;width:8px;height:8px;border-radius:50%;background:var(--ring)}
.stem.top::after{top:-4px}
.stem.bot::after{bottom:-4px}
.finding-text{width:340px;text-align:center;font-weight:700;font-size:17px;line-height:26px;color:var(--ink);white-space:nowrap}

/* eligibility */
.elig-art{left:115px;top:1331px;width:292px;height:286px;border-radius:50%;background:linear-gradient(#e9f2fb,#d2e6f7);border:1px dashed var(--line)}
.bracket{left:410px;top:1374px;width:40px;height:170px;border:2px solid var(--sky);border-left:none;border-radius:0 14px 14px 0}
.elig-tag{left:479px;top:1395px;background:var(--teal);color:var(--white);font-weight:800;font-size:24px;line-height:30px;padding:3px 16px;letter-spacing:.5px}
.elig-text{left:480px;top:1445px;width:680px;font-weight:500;font-size:18.6px;line-height:29px;color:var(--ink)}

/* study details */
.details{left:0;top:1648px;width:1200px;height:486px;background:var(--sky)}
.details .tab{position:absolute;left:443px;top:0;width:316px;height:56px}
.detail-list{list-style:none;position:absolute;border-left:2px dashed rgba(255,255,255,.7)}
.detail-list li{position:relative;color:var(--white);font-weight:600;font-size:21px;line-height:29px;padding-left:24px}
.detail-list li::before{content:"";position:absolute;left:-10px;top:6px;width:14px;height:14px;border:2px solid var(--white);border-radius:50%;background:var(--sky)}
.dl-left{left:130px;top:118px;width:440px}
.dl-right{left:643px;top:113px;width:450px}

/* audience */
.audience-tab{left:473px;top:2134px;width:308px;height:55px}
.aud-box{top:2244px;width:194px;height:141px;border:2px solid var(--sky);border-radius:8px;text-align:center;font-weight:600;font-size:16.5px;line-height:21px;color:var(--ink);padding:56px 4px 0;white-space:nowrap}
.aud-icon{top:2211px;width:72px;height:72px;border-radius:50%;display:flex;align-items:center;justify-content:center}
.aud-icon.sky{background:var(--sky)}
.aud-icon.navy{background:var(--navy)}

/* sponsor */
.sponsor-box{left:160px;top:2444px;width:966px;height:243px;border:2px solid #dfe6ee;border-radius:8px}
.uni-seal{left:86px;top:2444px;width:242px;height:242px;border-radius:50%;background:var(--navy);border:8px solid var(--sky);display:flex;flex-direction:column;align-items:center;justify-content:center;color:var(--white);font-weight:500;font-size:16px;text-align:center;line-height:24px}
.uni-seal b{font-weight:500;font-size:16px;letter-spacing:2px}
.sponsor-label{left:361px;top:2476px;color:var(--sky);font-weight:700;font-size:26px;line-height:36px}
.sponsor-text{left:362px;top:2514px;width:680px;font-weight:600;font-size:19px;line-height:29px;color:var(--ink)}
.partner{left:363px;top:2628px;display:flex;align-items:center;gap:8px;color:#666;font-weight:400;font-size:22px}
.partner i{width:28px;height:28px;background:#c9302c;display:block}

/* footer */
.footer{left:0;top:2739px;width:1200px;height:95px;background:var(--navy);display:flex;align-items:center;justify-content:center;gap:48px;color:var(--white);font-size:20px}
.footer strong{font-weight:600}
.mail{display:flex;align-items:center;gap:12px;font-weight:600}
.mail-dot{width:38px;height:38px;border-radius:50%;background:var(--sky);display:flex;align-items:center;justify-content:center}
</style>
</head>
<body>

<header class="abs masthead">
  <div class="abs brand"><span class="brand-dot"></span><span class="brand-name">PLUME</span></div>
  <h1 class="abs masthead-title">A feasibility study of standard dressings versus<br>negative-pressure wound therapy in the treatment of<br>adult patients having surgical incisions for hip fractures:<span>The PLUME randomized controlled trial</span></h1>
</header>

<h2 class="abs intro-heading">HIP FRACTURE SURGERY:<br>CAN ‘VACUUM’ DRESSINGS REDUCE<br>DEEP INFECTIONS?<span>(FEASIBILITY TRIAL)</span></h2>
<p class="abs intro-body">Adults &gt;65 years undergoing hip fracture surgery at 5<br>UK centres were randomised to standard dressings or<br>negative pressure ‘vacuum’ dressings (called iNPWT).<br>Deep infection (CDC-defined) was assessed at 30 &amp;<br>90 days; other outcomes like Health Related Quality of<br>Life were assessed at 120 days. The overall deep SSI<br>rate was ~4%; effect signals favoured iNPWT, and a<br>definitive trial was deemed feasible.</p>
<div class="abs intro-art" role="img" aria-label="Illustration of a pelvis with a hip implant beside an older man seated in a wheelchair"></div>

<section class="abs findings">
  <div class="tab tab-teal">FINDINGS</div>
</section>
<div class="abs track"></div>

<div class="abs node" style="left:124px;top:1053px"><svg width="60" height="52" viewBox="0 0 60 52" fill="none" stroke="#1f3864" stroke-width="2.5"><circle cx="30" cy="10" r="7"/><circle cx="14" cy="16" r="6"/><circle cx="46" cy="16" r="6"/><path d="M20 50V34a10 10 0 0 1 20 0v16M4 50V36a9 9 0 0 1 14-7M56 50V36a9 9 0 0 0-14-7"/></svg></div>
<div class="abs stem bot" style="left:181px;top:1166px"></div>
<p class="abs finding-text" style="left:12px;top:1178px">462 valid randomisations;<br>recruitment rate ~62% of<br>eligible cases.</p>

<p class="abs finding-text" style="left:289px;top:960px">Deep SSI at 30 days:<br>6.4% (standard) vs 1.9% (iNPWT) at<br>90 days: 6.4% vs 2.3%.</p>
<div class="abs stem top" style="left:458px;top:1050px"></div>
<div class="abs node" style="left:401px;top:1053px"><svg width="56" height="52" viewBox="0 0 56 52" fill="none" stroke="#1f3864" stroke-width="2.5"><rect x="3" y="7" width="42" height="38" rx="3"/><path d="M3 17h42M13 3v8M35 3v8M10 24h4M20 24h4M30 24h4M10 32h4M20 32h4M10 40h4"/><circle cx="44" cy="40" r="9" fill="#fff"/><path d="M44 35v5l3 3"/></svg></div>

<div class="abs node" style="left:696px;top:1053px"><svg width="44" height="56" viewBox="0 0 44 56" fill="none" stroke="#1f3864" stroke-width="2.5"><path d="M30 4a5 5 0 0 1 8 5 5 5 0 0 1-2 8L26 28M14 52a5 5 0 0 1-8-5 5 5 0 0 1 2-8l10-11"/><path d="M30 30l8 2M32 24l8-1"/></svg></div>
<div class="abs stem bot" style="left:753px;top:1166px"></div>
<p class="abs finding-text" style="left:584px;top:1178px">Overall 30-day deep SSI<br>4.2% for hip fracture<br>population</p>

<p class="abs finding-text" style="left:849px;top:958px">Feasibility confirmed for<br>a fully powered<br>effectiveness trial.</p>
<div class="abs stem top" style="left:1031px;top:1050px"></div>
<div class="abs node" style="left:974px;top:1053px"><svg width="44" height="56" viewBox="0 0 44 56" fill="none" stroke="#1f3864" stroke-width="2.5"><rect x="3" y="6" width="38" height="48" rx="3"/><rect x="14" y="2" width="16" height="8" rx="2" fill="#fff"/><path d="M22 16v10M17 21h10M10 34h4M18 34h16M10 42h4M18 42h16"/></svg></div>

<div class="abs elig-art" role="img" aria-label="Illustration of an older man in a wheelchair and an older woman with a walking stick"></div>
<div class="abs bracket"></div>
<div class="abs elig-tag">ELIGIBILITY CRITERIA</div>
<p class="abs elig-text">Inclusion: age &gt;65 years; undergoing any surgery for hip fracture.<br>Exclusion: undisplaced intracapsular fracture treated with<br>cannulated screws; other factors precluding participation.</p>

<section class="abs details">
  <div class="tab tab-navy">STUDY DETAILS</div>
  <ul class="detail-list dl-left">
    <li style="margin-bottom:32px">Design: Two-arm multicentre RCT<br>embedded in the GLaRN cohort</li>
    <li style="margin-bottom:32px">Sites: 5 UK centres</li>
    <li style="margin-bottom:32px">Participants: 462 randomised</li>
    <li>Recruitment: Jul 2017–Feb 2018</li>
  </ul>
  <ul class="detail-list dl-right">
    <li style="margin-bottom:32px">Follow-up to 120 days</li>
    <li style="margin-bottom:32px">Primary outcome: deep SSI at 30 &amp; 90<br>days (CDC)</li>
    <li style="margin-bottom:32px">Secondary: recruitment metrics, further<br>surgery, EQ-5D-5L, complications,<br>mobility, residential status</li>
    <li>Registration: ISRCTN48210937.</li>
  </ul>
</section>

<div class="abs tab tab-teal audience-tab">TARGET AUDIENCE</div>
<div class="abs aud-box" style="left:98px">Orthopaedic &amp;<br>Trauma<br>Clinicians</div>
<div class="abs aud-box" style="left:306px">Orthogeriatric<br>Teams</div>
<div class="abs aud-box" style="left:515px">Infection<br>Prevention Leads</div>
<div class="abs aud-box" style="left:723px">Commissioners</div>
<div class="abs aud-box" style="left:932px">Patient/Public<br>Audiences</div>
<div class="abs aud-icon sky" style="left:159px"><svg width="36" height="36" viewBox="0 0 36 36" fill="none" stroke="#fff" stroke-width="2.2"><circle cx="18" cy="11" r="7"/><path d="M4 34a14 14 0 0 1 28 0"/></svg></div>
<div class="abs aud-icon navy" style="left:367px"><svg width="38" height="36" viewBox="0 0 38 36" fill="none" stroke="#fff" stroke-width="2.2"><circle cx="19" cy="9" r="5"/><circle cx="8" cy="13" r="4"/><circle cx="30" cy="13" r="4"/><path d="M12 34V24a7 7 0 0 1 14 0v10M2 32v-6a6 6 0 0 1 8-5M36 32v-6a6 6 0 0 0-8-5"/></svg></div>
<div class="abs aud-icon sky" style="left:576px"><svg width="36" height="36" viewBox="0 0 36 36" fill="none" stroke="#fff" stroke-width="2.2"><path d="M6 30l14-14 4 4-14 14H6zM20 12l8-8 4 4-8 8M16 16l4 4"/></svg></div>
<div class="abs aud-icon navy" style="left:784px"><svg width="36" height="36" viewBox="0 0 36 36" fill="none" stroke="#fff" stroke-width="2.2"><circle cx="18" cy="11" r="7"/><path d="M4 34a14 14 0 0 1 28 0M18 22v8"/></svg></div>
<div class="abs aud-icon sky" style="left:993px"><svg width="36" height="36" viewBox="0 0 36 36" fill="none" stroke="#fff" stroke-width="2.2"><circle cx="18" cy="13" r="8"/><path d="M3 20c4 8 9 12 15 12s11-4 15-12"/></svg></div>

<div class="abs sponsor-box"></div>
<div class="abs uni-seal"><span>UNIVERSITY OF</span><b>CARROWBY</b></div>
<div class="abs sponsor-label">SPONSOR</div>
<p class="abs sponsor-text">Guild of Operative Surgeons/Halvern Ageing Trust (training<br>fellowship), Carrowby Biomedical Research Hub (infrastructure<br>support), Tessford Medical (device supply).</p>
<div class="abs partner"><i></i><span>CARROWBY INJURY &amp; ACUTE CARE</span></div>

<footer class="abs footer">
  <span>Chief Investigator: <strong>Elinor Vashti</strong></span>
  <span class="mail"><span class="mail-dot"><svg width="20" height="14" viewBox="0 0 20 14" fill="none" stroke="#fff" stroke-width="1.8"><rect x="1" y="1" width="18" height="12" rx="1"/><path d="M1 1l9 7 9-7"/></svg></span>elinor.vashti@carrowby-trials.example</span>
</footer>

</body>
</html>
```